DM - management consultant

Business card - contemporary design

Front info
Dorian Maples

(Address not necessary)
PO Box 7386
Belmont, CA 94002

(650) 555-0143
dm@dorianmapl.es

Twitter: dmq527
Facebook: /Dorian.Maples
Linkedin: /in/dorianmaples

Back or Front
www.dorianmaples.net
Facilitation & coaching, change management, strategic partnerships, business improvement

Target Market(s)

High tech businesses - mostly startups in Silicon Valley

Industry/Entity Type

Business

Font styles to use
Sans Serif

Colors

Designer to choose colors to be used in the design.

```html
<!DOCTYPE html>
<html lang="en">
<head>
<meta charset="utf-8">
<title>Dorian Maples – Business Card</title>
<link rel="stylesheet" href="https://fonts.googleapis.com/css2?family=Poiret+One&family=Gochi+Hand&display=swap">
<style>
  :root {
    --card-black: #000000;
    --ink-white: #ffffff;
    --band-ink: #111111;
    --pattern-tone-a: #3c3c3c;
    --pattern-tone-b: #242424;
    --icon-grey: #ffffff;
  }
  * { margin: 0; padding: 0; box-sizing: border-box; }
  html, body {
    width: 695px; height: 1200px; overflow: hidden;
    background: var(--card-black);
  }
  .card {
    position: relative; width: 695px; height: 1200px;
    background: var(--card-black); color: var(--ink-white);
    font-family: "Poiret One", sans-serif; overflow: hidden;
  }
  .pattern {
    position: absolute;
    background: linear-gradient(180deg, var(--pattern-tone-a), var(--pattern-tone-b));
  }
  .pattern--top-left { left: 12px; top: 0; width: 118px; height: 465px; }
  .pattern--bottom-right { left: 580px; top: 660px; width: 115px; height: 410px; }

  .name {
    position: absolute; left: 146px; top: 22px;
    font-size: 56px; font-variant: small-caps; letter-spacing: 2px;
    font-weight: 400; line-height: 1; white-space: nowrap;
  }
  .contact {
    position: absolute; left: 248px; font-size: 38px; letter-spacing: 2px;
    line-height: 1; white-space: nowrap;
  }
  .contact--phone { top: 102px; }
  .contact--email { top: 150px; font-size: 32px; text-transform: uppercase; }

  .services {
    position: absolute; left: 0; top: 505px; width: 695px; height: 120px;
    background: var(--ink-white); color: var(--band-ink);
    font-family: "Gochi Hand", sans-serif; font-size: 29px; line-height: 27px;
    text-align: center; display: flex; flex-direction: column;
    justify-content: center; letter-spacing: 1px;
  }

  .social { position: absolute; left: 80px; top: 783px; list-style: none; }
  .social__item {
    display: flex; align-items: center; height: 70px;
    font-size: 32px; letter-spacing: 2px; text-transform: uppercase;
    font-variant: small-caps;
  }
  .social__dot {
    width: 34px; height: 34px; border-radius: 50%;
    background: var(--icon-grey); margin-right: 22px; flex: none;
  }

  .website {
    position: absolute; left: 46px; top: 1100px;
    font-size: 46px; letter-spacing: 2px; font-variant: small-caps;
    white-space: nowrap; line-height: 1;
  }
</style>
</head>
<body>
  <main class="card">
    <div class="pattern pattern--top-left" role="img" aria-label="Column of white fleur-de-lis ornaments"></div>
    <div class="pattern pattern--bottom-right" role="img" aria-label="Column of white fleur-de-lis ornaments"></div>

    <h1 class="name">Dorian Maples</h1>
    <p class="contact contact--phone">(650) 555-0143</p>
    <p class="contact contact--email">dm@dorianmapl.es</p>

    <section class="services">
      <span>Facilitation &amp; Coaching</span>
      <span>Change Management</span>
      <span>Strategic Partnerships &amp;</span>
      <span>Business Improvement</span>
    </section>

    <ul class="social">
      <li class="social__item"><span class="social__dot"></span>dmq527</li>
      <li class="social__item"><span class="social__dot"></span>Dorian.Maples</li>
      <li class="social__item"><span class="social__dot"></span>DorianMaples</li>
    </ul>

    <p class="website">www.DorianMaples.net</p>
  </main>
</body>
</html>
```